Gombrevo business card

Based on company logo and website given , to design a business card temple. Slogan "Your furry friends deserves the best"
Color style please refer to our website

```html
<!DOCTYPE html>
<html lang="en">
<head>
<meta charset="utf-8">
<title>Gombrevo business card</title>
<link rel="stylesheet" href="https://fonts.googleapis.com/css2?family=Montserrat:wght@400;600;700&display=swap">
<style>
  :root {
    --olive: #bdb033;
    --paper: #ffffff;
    --ink: #4a4a4a;
    --muted: #6b6b6b;
    --backdrop: #2b2b2b;
  }
  html, body {
    margin: 0;
    padding: 0;
    width: 1200px;
    height: 900px;
    overflow: hidden;
    background: var(--backdrop);
    font-family: "Montserrat", sans-serif;
  }
  .canvas {
    width: 1200px;
    height: 900px;
    display: flex;
    flex-direction: column;
    align-items: center;
    justify-content: center;
    gap: 50px;
  }
  .card {
    width: 630px;
    height: 360px;
    position: relative;
    box-sizing: border-box;
    box-shadow: 0 12px 30px rgba(0,0,0,0.45);
  }
  .card-front { background: var(--paper); }
  .card-back { background: var(--olive); }

  .holder {
    position: absolute;
    left: 44px;
    top: 44px;
  }
  .holder-name {
    margin: 0;
    font-size: 22px;
    font-weight: 700;
    letter-spacing: 0.5px;
    color: var(--olive);
    text-transform: uppercase;
  }
  .holder-title {
    margin: 2px 0 0;
    font-size: 16px;
    font-weight: 400;
    color: var(--muted);
  }

  .wordmark {
    font-weight: 700;
    letter-spacing: -1px;
    margin: 0;
  }
  .card-front .wordmark {
    position: absolute;
    right: 44px;
    top: 118px;
    font-size: 52px;
    color: var(--olive);
  }

  .address {
    position: absolute;
    left: 300px;
    top: 196px;
    margin: 0;
    font-style: normal;
    font-size: 15px;
    line-height: 21px;
    color: var(--ink);
  }
  .contacts {
    position: absolute;
    left: 280px;
    top: 252px;
    margin: 0;
    padding: 0;
    list-style: none;
    font-size: 15px;
    line-height: 24px;
    color: var(--ink);
  }
  .contacts li {
    display: flex;
    align-items: center;
    gap: 8px;
  }
  .contacts svg {
    width: 13px;
    height: 13px;
    fill: var(--olive);
    flex: none;
  }

  .card-back .wordmark {
    position: absolute;
    left: 0;
    right: 0;
    top: 118px;
    text-align: center;
    font-size: 76px;
    color: var(--paper);
  }
  .slogan {
    position: absolute;
    left: 0;
    right: 0;
    top: 238px;
    margin: 0;
    text-align: center;
    font-size: 17px;
    font-weight: 400;
    letter-spacing: 0.5px;
    color: var(--paper);
  }
</style>
</head>
<body>
<main class="canvas">
  <section class="card card-front" aria-label="Business card front">
    <div class="holder">
      <h1 class="holder-name">Dale Ormsby</h1>
      <p class="holder-title">President</p>
    </div>
    <p class="wordmark">Gombrevo</p>
    <address class="address">18720 Lantern Cove Way<br>Harbor Vale CA 90470</address>
    <ul class="contacts">
      <li>
        <svg viewBox="0 0 24 24" aria-hidden="true"><path d="M6.6 10.8a15.1 15.1 0 0 0 6.6 6.6l2.2-2.2c.3-.3.7-.4 1-.2 1.1.4 2.3.6 3.6.6.6 0 1 .4 1 1V20c0 .6-.4 1-1 1A17 17 0 0 1 3 4c0-.6.4-1 1-1h3.5c.6 0 1 .4 1 1 0 1.3.2 2.5.6 3.6.1.3 0 .7-.2 1z"/></svg>
        555-310-0187
      </li>
      <li>
        <svg viewBox="0 0 24 24" aria-hidden="true"><path d="M2 5h20v14H2zm2 2v.5l8 5 8-5V7l-8 5z"/></svg>
        dormsby@gombrevo.com
      </li>
      <li>
        <svg viewBox="0 0 24 24" aria-hidden="true"><path d="M12 2a10 10 0 1 0 0 20 10 10 0 0 0 0-20zm6.9 6h-2.9a15 15 0 0 0-1.4-3.6A8 8 0 0 1 18.9 8zM12 4c.8 1.2 1.5 2.5 1.9 4h-3.8c.4-1.5 1.1-2.8 1.9-4zM4.3 14a8 8 0 0 1 0-4h3.4a16 16 0 0 0 0 4zm.8 2h2.9c.3 1.3.8 2.5 1.4 3.6A8 8 0 0 1 5.1 16zM8 8H5.1a8 8 0 0 1 4.3-3.6C8.8 5.5 8.3 6.7 8 8zm4 12c-.8-1.2-1.5-2.5-1.9-4h3.8c-.4 1.5-1.1 2.8-1.9 4zm2.3-6H9.7a14 14 0 0 1 0-4h4.6a14 14 0 0 1 0 4zm.3 5.6c.6-1.1 1.1-2.3 1.4-3.6h2.9a8 8 0 0 1-4.3 3.6zm1.7-5.6a16 16 0 0 0 0-4h3.4a8 8 0 0 1 0 4z"/></svg>
        www.gombrevo.com
      </li>
    </ul>
  </section>

  <section class="card card-back" aria-label="Business card back">
    <p class="wordmark">Gombrevo</p>
    <p class="slogan">Your furry friends deserves the best</p>
  </section>
</main>
</body>
</html>
```